Adult Literacy Program - flyer to attract volunteers and students

We want a flyer that is engaging, colorful, modern and will appeal to our primary audience of adults aged 40-60. We are trying to attract both prospective volunteers (typically age 50+, mostly women) and students (typically aged 40+).
The flyer should feature diverse people working together in pairs of two, reading or talking, with a workbook or some reading material in front of them.

Our organization trains tutors to work one-on-one with adults who are learning how to read. Most of our adult students are non-native speakers of English. Many are of Haitian or Hispanic origin, so we would like some people who represent that demographic.

The Flyer should represent reading, learning, literacy, knowledge, growth,
and opportunities.
Our students are learning to read so they can advance their job opportunities.

Target Market(s)

Adults aged 40-60, primarily women, retired, volunteers

Industry/Entity Type

Education

Font styles to use
Serif
Sans Serif

Colors

Designer to choose colors to be used in the design.

Requirements
Must have
• - UPDATE: Should be designed as a TRI-FOLD brochure on 8.5 x 11 inch paper that will be folded into thirds.
• - Images of diverse people, women and men, who look Hispanic, Haitian and other nationalities as well as Caucasian.
• - Our logo on the front cover
Nice to have
• The sample flyer is very boring and dry! We are open to different ways of presenting the text.

```html
<!DOCTYPE html>
<html lang="en">
<head>
<meta charset="utf-8">
<title>Readwell Partners – Tri-fold Brochure</title>
<link href="https://fonts.googleapis.com/css2?family=Marcellus&family=Open+Sans:ital,wght@0,400;0,600;0,700;1,400&display=swap" rel="stylesheet">
<style>
  :root {
    --page-bg: #eef1f5;
    --paper: #ffffff;
    --ink: #111111;
    --brand-blue: #1e7fd6;
    --sky: #3fb4f5;
    --deep-blue: #0d5fd8;
    --light-blue: #9fdcff;
    --fold-shade: #d7d7d7;
    --photo-warm-1: #c9a98e;
    --photo-warm-2: #7d8a94;
    --photo-green-1: #b8b59a;
    --photo-green-2: #3fa9b8;
    --photo-lib-1: #c7c9cc;
    --photo-lib-2: #6b7f96;
  }
  * { margin: 0; padding: 0; box-sizing: border-box; }
  html, body { width: 1200px; height: 1080px; overflow: hidden; }
  body { background: var(--page-bg); font-family: "Open Sans", Arial, sans-serif; color: var(--ink); position: relative; }

  .brochure { position: absolute; left: 0; top: 93px; width: 1200px; height: 894px; background: var(--paper); overflow: hidden; }
  .panel { position: absolute; top: 0; width: 400px; height: 894px; overflow: hidden; }
  .panel--cover { left: 0; }
  .panel--tutors { left: 400px; }
  .panel--students { left: 800px; border-left: 1px solid #cfcfcf; }

  .fold-shade { position: absolute; top: 0; height: 100%; }
  .panel--cover .fold-shade { left: 256px; width: 144px; background: linear-gradient(90deg, #f4f4f4, var(--fold-shade)); }
  .panel--tutors .fold-shade { left: 258px; width: 142px; background: linear-gradient(90deg, #f6f6f6, var(--fold-shade)); }

  .swoosh { position: absolute; left: 0; top: 0; width: 400px; height: 894px; }

  .brand { position: absolute; left: 80px; width: 240px; text-align: center; font-family: "Open Sans", Arial, sans-serif; font-weight: 700; color: var(--brand-blue); letter-spacing: 1px; }
  .brand__dot { display: block; margin: 0 auto 10px; width: 44px; height: 44px; border-radius: 50%; background: var(--brand-blue); }
  .brand__name { display: block; font-size: 22px; line-height: 1.15; }
  .panel--cover .brand { top: 70px; }
  .panel--students .brand { top: 708px; }

  .heading { font-family: "Marcellus", Georgia, serif; font-weight: 400; color: var(--ink); letter-spacing: 1px; line-height: 40px; }
  .cover__title { position: absolute; left: 26px; top: 226px; font-size: 37px; }
  .cover__lead { position: absolute; left: 26px; top: 280px; font-size: 16px; font-weight: 600; line-height: 29px; letter-spacing: .3px; }

  .photo { position: absolute; }
  .photo--pair-main { left: 24px; top: 381px; width: 352px; height: 304px; border-radius: 0 170px 0 160px; background: linear-gradient(135deg, var(--photo-warm-1), var(--photo-warm-2)); }
  .photo--pair-small { left: 30px; top: 691px; width: 210px; height: 180px; border-radius: 110px 0 0 0; background: linear-gradient(135deg, #d8c3a8, #8a6f6a); }
  .photo--pair-men { left: 250px; top: 691px; width: 126px; height: 109px; border-top-right-radius: 70px; background: linear-gradient(135deg, #b7c4cf, #6e8aa3); }

  .tutors__title { position: absolute; left: 16px; top: 22px; font-size: 37px; }
  .list { position: absolute; list-style: none; font-size: 16px; font-weight: 600; letter-spacing: .3px; }
  .tutors__list { left: 16px; top: 86px; width: 370px; }
  .tutors__list li { position: relative; padding-left: 10px; line-height: 23px; margin-bottom: 23px; }
  .tutors__list li::before, .students__list li.bullet::before { content: "·"; position: absolute; left: 0; }
  .tutors__list li.last { margin-bottom: 0; }
  .tutors__list li.close { padding-left: 5px; margin: 0; }
  .tutors__list li.close::before { content: none; }
  .photo--tutor-pair { left: 17px; top: 451px; width: 367px; height: 315px; border-radius: 0 180px 0 180px; background: linear-gradient(135deg, var(--photo-green-1), var(--photo-green-2)); }

  .students__title { position: absolute; left: 24px; top: 20px; font-size: 37px; }
  .students__list { left: 24px; top: 63px; width: 370px; }
  .students__list li { position: relative; line-height: 23px; }
  .students__list li.bullet { padding-left: 10px; }
  .students__list li.topic { font-weight: 400; font-style: italic; }
  .students__list li.close { padding-left: 5px; }
  .photo--study-group { left: 42px; top: 290px; width: 304px; height: 260px; border-radius: 150px 150px 0 150px; background: linear-gradient(135deg, var(--photo-lib-1), var(--photo-lib-2)); }
  .students__cta { position: absolute; left: 0; width: 400px; top: 556px; text-align: center; font-size: 27px; font-weight: 700; letter-spacing: 1px; }
  .contact { position: absolute; left: 0; width: 400px; top: 614px; text-align: center; font-size: 14px; font-weight: 600; line-height: 21px; letter-spacing: .2px; }
</style>
</head>
<body>
  <main class="brochure">
    <section class="panel panel--cover">
      <div class="fold-shade"></div>
      <svg class="swoosh" viewBox="0 0 400 894" aria-hidden="true">
        <path d="M0 0 H300 C200 40 110 120 60 230 C30 300 14 380 0 460 Z" fill="var(--sky)"/>
        <path d="M0 0 H170 C100 60 40 150 0 260 Z" fill="var(--deep-blue)" opacity=".55"/>
        <path d="M220 0 H300 C230 50 150 140 100 260 C150 130 190 60 220 0 Z" fill="var(--light-blue)"/>
        <path d="M0 460 C10 380 30 330 60 290 C40 360 20 420 0 520 Z" fill="var(--light-blue)"/>
      </svg>
      <div class="brand"><span class="brand__dot"></span><span class="brand__name">READWELL<br>PARTNERS</span></div>
      <h1 class="heading cover__title">VOLUNTEER</h1>
      <p class="cover__lead">Enrich a Life!<br>Help an adult learn to read, write<br>or speak English</p>
      <div class="photo photo--pair-main" role="img" aria-label="Photo of a smiling volunteer tutor in a library with learners reading at a table"></div>
      <div class="photo photo--pair-small" role="img" aria-label="Photo of a tutor and student working together over a workbook"></div>
      <div class="photo photo--pair-men" role="img" aria-label="Photo of two men reading together in a library"></div>
    </section>

    <section class="panel panel--tutors">
      <div class="fold-shade"></div>
      <h2 class="heading tutors__title">TUTORS</h2>
      <ul class="list tutors__list">
        <li>No special skills or degrees needed —<br>just a degree of caring!</li>
        <li>Training offered throughout the year</li>
        <li>Tutors meet students weekly at a library</li>
        <li>Instructional materials provided</li>
        <li class="last">Ongoing support available</li>
        <li class="close">Teach an adult to read and you’ll change<br>a life forever.</li>
      </ul>
      <div class="photo photo--tutor-pair" role="img" aria-label="Photo of two smiling women sitting outdoors with an open book"></div>
    </section>

    <section class="panel panel--students">
      <svg class="swoosh" viewBox="0 0 400 894" aria-hidden="true">
        <path d="M400 520 C370 600 360 700 380 894 H400 Z" fill="var(--light-blue)"/>
        <path d="M0 894 C60 820 160 760 300 740 C350 735 380 745 400 760 V894 Z" fill="var(--sky)"/>
        <path d="M120 894 C180 830 270 800 400 810 V894 Z" fill="var(--deep-blue)" opacity=".6"/>
      </svg>
      <h2 class="heading students__title">STUDENTS</h2>
      <ul class="list students__list">
        <li>Students are adults in need of</li>
        <li class="topic">basic literacy skills</li>
        <li class="topic">pre-GED skills</li>
        <li class="topic">conversational English</li>
        <li class="bullet">Tutoring is free of charge</li>
        <li class="bullet">Tutoring is one-on-one</li>
        <li class="bullet">Flexible scheduling during library hours</li>
        <li class="bullet">Lessons focus on student goals</li>
        <li class="close">If you can read, you can tutor!</li>
      </ul>
      <div class="photo photo--study-group" role="img" aria-label="Photo of adult learners and tutors talking with books at a library table"></div>
      <p class="students__cta">Don’t waste a moment!</p>
      <p class="contact">Contact us today to learn more.<br>Volunteer Desk: 555-014-2200<br>Eastfield, Millbrook &amp; Lakeview: 555-018-7300<br>email: learn@readwellpartners.org</p>
      <div class="brand"><span class="brand__dot"></span><span class="brand__name">READWELL<br>PARTNERS</span></div>
    </section>
  </main>
</body>
</html>
```